Nera Bloom Fitness Coaching Project

I am a personal trainer based in London. My services include one-on-one PT sessions, bootcamps.
I would like the design to be minimalistic. With light colours: white, pink, purple.
I specialise in weight loss, flexibility, mobility.

Orla Pemvick
Personal Trainer
Email: orla.pemvick@tovamail.com
tel: 07400918243
Instagram: Nera Bloom

Target Market(s)

adults, mostly females (age 18-50).

Industry/Entity Type

Fitness

Contact Information for Business Card

Orla Pemvick
Personal Trainer
tel: 07400918243
Instagram: Nera Bloom

Font styles to use
Serif

Colors
eea4c8
fbd4d5
fdf9cf
cfeae6
cee9f5

Requirements
Nice to have
• minimalistic style
• easy to read and remember

```html
<!DOCTYPE html>
<html lang="en">
<head>
<meta charset="utf-8">
<title>Orla Pemvick – Personal Trainer Business Card</title>
<link href="https://fonts.googleapis.com/css2?family=Cormorant+Garamond:wght@500&family=Questrial&family=Tinos&display=swap" rel="stylesheet">
<style>
  :root {
    --bg: #e6e4e8;
    --card-white: #fbfbfc;
    --rule: #4a4a4a;
    --ink: #5a5a5e;
    --icon-pink: #d9a2d6;
    --wash: rgba(255, 255, 255, 0.28);
    --name-ink: #f4f2f4;
    --title-ink: #2d2d30;
    --tag-ink: #1f1f22;
    --tag-band: rgba(240, 240, 242, 0.82);
    --divider: #f2f2f4;
  }
  * { margin: 0; padding: 0; box-sizing: border-box; }
  html, body {
    width: 1200px;
    height: 997px;
    overflow: hidden;
    background: var(--bg);
  }
  .card {
    position: absolute;
    left: 240px;
    width: 720px;
    height: 430px;
    border-radius: 26px;
    overflow: hidden;
    box-shadow: 0 6px 22px rgba(0, 0, 0, 0.12);
  }

  /* Back of card */
  .card-back {
    top: 48px;
    background: var(--card-white);
  }
  .card-back .rule {
    position: absolute;
    left: 50%;
    width: 2px;
    background: var(--rule);
  }
  .card-back .rule-top { top: 0; height: 152px; }
  .card-back .rule-bottom { top: 286px; height: 144px; }
  .contact-list {
    position: absolute;
    top: 166px;
    left: 262px;
    list-style: none;
    font-family: "Tinos", "Times New Roman", serif;
    font-size: 21px;
    color: var(--ink);
  }
  .contact-list li {
    display: flex;
    align-items: center;
    gap: 12px;
    height: 36px;
  }
  .contact-icon {
    width: 22px;
    height: 22px;
    flex: none;
  }

  /* Front of card */
  .card-front {
    top: 516px;
  }
  .card-front .collage {
    position: absolute;
    inset: 0;
    width: 720px;
    height: 430px;
  }
  .brand-name {
    position: absolute;
    top: 92px;
    left: 196px;
    font-family: "Cormorant Garamond", Georgia, serif;
    font-weight: 500;
    font-size: 44px;
    letter-spacing: 2px;
    color: var(--name-ink);
    text-transform: uppercase;
    text-shadow: 0 0 1px rgba(0,0,0,0.55);
    line-height: 1;
  }
  .brand-title {
    position: absolute;
    top: 140px;
    left: 236px;
    font-family: "Questrial", Arial, sans-serif;
    font-size: 17px;
    letter-spacing: 5px;
    color: var(--title-ink);
  }
  .specialities {
    position: absolute;
    top: 312px;
    left: 420px;
    font-family: "Questrial", Arial, sans-serif;
    font-size: 17px;
    color: var(--tag-ink);
    transform: rotate(5.7deg);
    transform-origin: left center;
    white-space: nowrap;
  }
</style>
</head>
<body>

<section class="card card-back" aria-label="Card back">
  <span class="rule rule-top"></span>
  <ul class="contact-list">
    <li>
      <svg class="contact-icon" viewBox="0 0 22 22" aria-hidden="true">
        <circle cx="11" cy="11" r="11" fill="var(--icon-pink)"/>
        <path d="M7.2 6.2 L9 6 L10 8.6 L8.9 9.4 Q9.8 11.6 12.4 13 L13.3 11.9 L15.9 12.9 L15.7 14.7 Q14.9 15.9 13.2 15.6 Q8.2 14.2 6.5 8.6 Q6.3 7 7.2 6.2 Z" fill="#fff"/>
      </svg>
      <span>07400918243</span>
    </li>
    <li>
      <svg class="contact-icon" viewBox="0 0 22 22" aria-hidden="true">
        <circle cx="11" cy="11" r="11" fill="var(--icon-pink)"/>
        <rect x="5.5" y="7" width="11" height="8" rx="1" fill="#fff"/>
        <path d="M5.8 7.4 L11 11.4 L16.2 7.4" stroke="var(--icon-pink)" stroke-width="1.1" fill="none"/>
      </svg>
      <span>orla.pemvick@tovamail.com</span>
    </li>
    <li>
      <svg class="contact-icon" viewBox="0 0 22 22" aria-hidden="true">
        <circle cx="11" cy="11" r="11" fill="var(--icon-pink)"/>
      </svg>
      <span>snapgrid.com/Nera_Bloom</span>
    </li>
  </ul>
  <span class="rule rule-bottom"></span>
</section>

<section class="card card-front" aria-label="Card front">
  <svg class="collage" viewBox="0 0 720 430" aria-hidden="false">
    <defs>
      <linearGradient id="portrait-tone" x1="0" y1="0" x2="1" y2="1">
        <stop offset="0" stop-color="#8d8a8c"/>
        <stop offset="0.45" stop-color="#b08a72"/>
        <stop offset="1" stop-color="#d9cfd0"/>
      </linearGradient>
      <linearGradient id="handstand-tone" x1="0" y1="0" x2="1" y2="1">
        <stop offset="0" stop-color="#e5a9a7"/>
        <stop offset="0.6" stop-color="#b8857d"/>
        <stop offset="1" stop-color="#d7d2d3"/>
      </linearGradient>
      <linearGradient id="stretch-tone" x1="0" y1="0" x2="0.7" y2="1">
        <stop offset="0" stop-color="#e67ab4"/>
        <stop offset="0.45" stop-color="#e8a2c6"/>
        <stop offset="0.55" stop-color="#7fd0c8"/>
        <stop offset="1" stop-color="#c6d0d0"/>
      </linearGradient>
      <linearGradient id="street-tone" x1="0" y1="0" x2="1" y2="1">
        <stop offset="0" stop-color="#d3d0d2"/>
        <stop offset="1" stop-color="#c7c4c6"/>
      </linearGradient>
    </defs>

    <polygon role="img" aria-label="Photo area: trainer smiling with curly hair in a floral top"
             points="0,0 300,0 720,170 720,330 0,70" fill="url(#portrait-tone)"/>
    <polygon role="img" aria-label="Photo area: trainer doing a handstand against a pink wall"
             points="300,0 720,0 720,170" fill="url(#handstand-tone)"/>
    <polygon role="img" aria-label="Photo area: trainer stretching in front of a pink and teal wall"
             points="0,70 720,330 720,430 0,430" fill="url(#stretch-tone)"/>
    <polygon role="img" aria-label="Photo area: pale street pavement"
             points="420,222 720,330 720,430 520,430" fill="url(#street-tone)" opacity="0.75"/>

    <line x1="300" y1="0" x2="720" y2="170" stroke="var(--divider)" stroke-width="5"/>
    <line x1="0" y1="70" x2="720" y2="330" stroke="var(--divider)" stroke-width="5"/>
    <polygon points="400,268 720,300 720,338 400,306" fill="var(--tag-band)"/>

    <rect x="0" y="0" width="720" height="430" fill="var(--wash)"/>
  </svg>

  <h1 class="brand-name">Orla Pemvick</h1>
  <p class="brand-title">Personal Trainer</p>
  <p class="specialities">Weight Loss • Flexibility • Mobility</p>
</section>

</body>
</html>
```